Medical clinic Flyer for Tovren Medical clinic in Chilliwack, BC

Need a double sided flyer design sized 5.5" x 8.5'' for a medical clinic. The flyer attached for Marlow Crest clinic is a good example of what we are looking for.

We need to focus on advertising this clinic as being a walk in clinic with short wait time. We need to make "walk in clinic Now open" eye catching.

We need to include the following messages:
1. Full Family Practice.
2. Accepting new patients.
3. Walk in clinic open Monday to Friday 9am to 4pm.
4. Short wait times.
5. No appointment needed
6.Check out our state of the art Medical clinic.
7. Velnox, Dermal Fillers, and Corvessa available (Physician Lead)

Target Market(s)

Residents of Chilliwack, BC.

Industry/Entity Type

Healthcare

Requirements
Must have
• Phone number: 18775206348
Addres: 4519 Birchwold Trail Pkwy Unit#312, Chilliwack, BC, V2R 0K7
Nice to have
• Location Map

```html
<!DOCTYPE html>
<html lang="en">
<head>
<meta charset="utf-8">
<title>Tovren Medical Centre – Walk In Clinic Flyer</title>
<link rel="stylesheet" href="https://fonts.googleapis.com/css2?family=Archivo:wght@800;900&family=Open+Sans:wght@400;600;700&display=swap">
<style>
  :root {
    --navy: #0c2a48;
    --blue: #1a5c9a;
    --red: #c21f32;
    --white: #ffffff;
    --ink: #1b1b1b;
    --page: #e9e9e9;
  }
  * { margin: 0; padding: 0; box-sizing: border-box; }
  html, body { width: 1048px; height: 1200px; overflow: hidden; background: var(--page); }
  body { position: relative; font-family: "Open Sans", sans-serif; color: var(--ink); }

  .flyer {
    position: absolute; left: 173px; width: 850px; height: 550px;
    background: var(--white); overflow: hidden;
    transform: scale(0.826); transform-origin: top left;
    box-shadow: 0 6px 18px rgba(0,0,0,.25);
  }
  .flyer--front { top: 107px; }
  .flyer--back { top: 625px; }
  .abs { position: absolute; }

  .brand { display: flex; align-items: center; gap: 12px; }
  .brand__mark { width: 46px; height: 46px; border-radius: 50%; background: var(--navy); flex: none; }
  .brand__name {
    font-family: "Open Sans", sans-serif; font-weight: 700; color: var(--red);
    font-size: 27px; line-height: 1.05; text-transform: uppercase; letter-spacing: .5px;
  }

  /* front */
  .front__shapes { left: 0; top: 0; }
  .front__logo { left: 42px; top: 48px; }
  .front__kicker { left: 20px; top: 136px; font-family: "Archivo", sans-serif; font-weight: 900; font-size: 36px; color: var(--blue); letter-spacing: .3px; }
  .front__headline { left: 22px; top: 176px; font-family: "Archivo", sans-serif; font-weight: 900; font-size: 50px; color: var(--white); letter-spacing: 1px; line-height: 60px; }
  .services { left: 28px; top: 248px; list-style: none; color: var(--white); font-size: 15.5px; font-weight: 600; width: 390px; }
  .services li { position: relative; padding-left: 17px; line-height: 18px; margin-bottom: 7.8px; }
  .services li::before { content: ""; position: absolute; left: 0; top: 5px; width: 8px; height: 8px; border-radius: 50%; background: var(--blue); }
  .front__doctors { left: 27px; top: 464px; font-family: "Open Sans", sans-serif; font-weight: 700; font-size: 23px; color: var(--white); letter-spacing: .2px; }
  .contact-bar { left: 30px; top: 518px; width: 800px; display: flex; align-items: center; font-size: 13.5px; font-weight: 600; color: var(--ink); }
  .contact-bar__item { display: flex; align-items: center; gap: 9px; }
  .contact-bar__item svg { flex: none; }
  .contact-bar__item--address { margin-right: 30px; }
  .contact-bar__item--phone { margin-right: 24px; }

  /* back */
  .back__logo { left: 30px; top: 26px; }
  .back__headline { left: 460px; top: 16px; width: 380px; text-align: center; font-family: "Open Sans", sans-serif; font-weight: 700; font-size: 32px; line-height: 34px; color: var(--blue); }
  .photo { position: absolute; }
  .photo--map { left: 0; top: 98px; width: 425px; height: 204px; background: linear-gradient(135deg, #eef1f3 0%, #dfe7ee 55%, #a9c6e8 100%); }
  .photo--storefront { left: 425px; top: 98px; width: 425px; height: 204px; background: linear-gradient(180deg, #b9aa96 0%, #8a7a68 45%, #cfd6db 60%, #8d8f92 100%); }
  .photo--interior { left: 0; top: 352px; width: 425px; height: 198px; background: linear-gradient(160deg, #d8dcdf 0%, #b8bdc2 50%, #6f7478 100%); }
  .photo--family { left: 329px; top: 368px; width: 130px; height: 130px; border-radius: 50%; border: 4px solid var(--white); background: linear-gradient(160deg, #e3e6ea, #b9a48e); }
  .back__band { left: 0; top: 302px; width: 850px; height: 50px; background: var(--red); color: var(--white); font-weight: 700; font-size: 23.5px; line-height: 50px; text-align: center; letter-spacing: .3px; }
  .back__panel { left: 425px; top: 352px; width: 425px; height: 198px; background: var(--navy); }
  .back__note { left: 425px; top: 378px; width: 425px; text-align: center; color: var(--white); font-size: 15.5px; line-height: 21px; }
  .back__cta { left: 425px; top: 432px; width: 425px; text-align: center; color: var(--white); font-weight: 700; font-size: 18.5px; letter-spacing: .4px; }
  .phone-pill { left: 498px; top: 466px; width: 286px; height: 28px; border-radius: 14px; background: var(--red); color: var(--white); display: flex; align-items: center; justify-content: center; gap: 14px; font-weight: 600; font-size: 20px; letter-spacing: .5px; }
  .back__address { left: 425px; top: 506px; width: 425px; text-align: center; color: var(--white); font-size: 13.5px; font-weight: 600; }
</style>
</head>
<body>

<section class="flyer flyer--front">
  <svg class="abs front__shapes" width="850" height="550" viewBox="0 0 850 550">
    <defs>
      <clipPath id="hero-clip"><circle cx="705" cy="190" r="290"/></clipPath>
    </defs>
    <rect x="0" y="198" width="850" height="300" fill="var(--navy)"/>
    <rect x="0" y="0" width="850" height="198" fill="var(--white)"/>
    <polygon points="330,198 850,198 850,235 345,235" fill="var(--navy)"/>
    <rect x="0" y="462" width="520" height="36" fill="var(--blue)"/>
    <circle cx="705" cy="190" r="304" fill="var(--red)"/>
    <circle cx="705" cy="190" r="297" fill="var(--white)"/>
    <circle cx="708" cy="186" r="294" fill="var(--navy)"/>
    <rect x="0" y="498" width="850" height="52" fill="var(--white)"/>
    <polygon points="0,178 330,178 345,235 0,235" fill="var(--red)"/>
    <g clip-path="url(#hero-clip)" role="img" aria-label="Photo of a smiling nurse listening with a stethoscope to a young girl holding a teddy bear">
      <rect x="400" y="-100" width="600" height="600" fill="url(#hero-tone)"/>
    </g>
    <linearGradient id="hero-tone" x1="0" y1="0" x2="1" y2="1">
      <stop offset="0" stop-color="#f3f1ee"/>
      <stop offset=".55" stop-color="#e6dcd2"/>
      <stop offset="1" stop-color="#c9c3bd"/>
    </linearGradient>
    <circle cx="522" cy="430" r="75" fill="var(--white)"/>
    <circle cx="522" cy="430" r="71" fill="url(#room-tone)" role="img" aria-label="Photo of a modern examination room with an exam bed"/>
    <linearGradient id="room-tone" x1="0" y1="0" x2="0" y2="1">
      <stop offset="0" stop-color="#e9ebec"/>
      <stop offset=".6" stop-color="#b6bbbf"/>
      <stop offset="1" stop-color="#7a7f84"/>
    </linearGradient>
  </svg>

  <div class="abs brand front__logo">
    <span class="brand__mark"></span>
    <span class="brand__name">Tovren<br>Medical Centre</span>
  </div>

  <h2 class="abs front__kicker">WALK IN CLINIC</h2>
  <h1 class="abs front__headline">NOW OPEN</h1>

  <ul class="abs services">
    <li>Full Family Practice</li>
    <li>Accepting new patients</li>
    <li>Walk in clinic open Monday to Friday 9am to 4pm</li>
    <li>Short wait times</li>
    <li>No appointment needed</li>
    <li>Check out our state of the art Medical clinic</li>
    <li>Velnox, Dermal Fillers, and Corvessa available (Physician Lead)</li>
  </ul>

  <p class="abs front__doctors">DOCTORS AVAILABLE!</p>

  <div class="abs contact-bar">
    <span class="contact-bar__item contact-bar__item--address">
      <svg width="18" height="18" viewBox="0 0 18 18"><circle cx="9" cy="9" r="9" fill="var(--blue)"/><path d="M9 4.5 4.5 8.5h1.4v4.5h2.3v-3h1.6v3h2.3V8.5h1.4z" fill="#fff"/></svg>
      4519 Birchwold Trail Pkwy Unit#312, Chilliwack, BC, V2R 0K7
    </span>
    <span class="contact-bar__item contact-bar__item--phone">
      <svg width="18" height="18" viewBox="0 0 18 18"><circle cx="9" cy="9" r="9" fill="var(--blue)"/><path d="M6.5 4.5c.6 0 1.4 1.7 1.4 2.2s-.8.8-.8 1.2c0 .8 1.6 2.9 2.8 3 .4 0 .7-.8 1.2-.8s2.1.8 2.1 1.4-1 1.6-2 1.6c-2.6 0-6.2-3.9-6.2-6.4 0-1 .9-2.2 1.5-2.2z" fill="#fff"/></svg>
      18775206348
    </span>
    <span class="contact-bar__item">
      <svg width="18" height="18" viewBox="0 0 18 18"><circle cx="9" cy="9" r="9" fill="var(--blue)"/><g fill="none" stroke="#fff" stroke-width="1"><circle cx="9" cy="9" r="5"/><ellipse cx="9" cy="9" rx="2.2" ry="5"/><path d="M4 9h10M5 6.5h8M5 11.5h8"/></g></svg>
      www.tovrenmedical.com
    </span>
  </div>
</section>

<section class="flyer flyer--back">
  <div class="abs brand back__logo">
    <span class="brand__mark"></span>
    <span class="brand__name">Tovren<br>Medical Centre</span>
  </div>
  <h2 class="abs back__headline">YOU HELTH<br>IS OUR PRIORITY</h2>

  <div class="photo photo--map" role="img" aria-label="Location map showing the clinic near the river and nearby shops in Chilliwack"></div>
  <div class="photo photo--storefront" role="img" aria-label="Photo of the clinic storefront with glass doors and a pharmacy next door"></div>

  <p class="abs back__band">PHYSICIANS ACCEPTING NEW PATIENTS, WALK-INS WELCOME!</p>

  <div class="photo photo--interior" role="img" aria-label="Photo of the clinic reception desk and waiting room chairs"></div>
  <div class="abs back__panel"></div>
  <div class="photo photo--family" role="img" aria-label="Photo of a smiling family with a doctor"></div>

  <p class="abs back__note">Come see us at our new location!<br>We are in the samee complex as Vesta Lab.</p>
  <p class="abs back__cta">PLEASE CALL OR VISIT US TODAY!</p>
  <div class="abs phone-pill">
    <svg width="20" height="20" viewBox="0 0 20 20"><circle cx="10" cy="10" r="8.5" fill="none" stroke="#fff" stroke-width="1.2"/><path d="M7.6 5.5c.6 0 1.3 1.6 1.3 2.1s-.8.8-.8 1.1c0 .8 1.5 2.7 2.6 2.8.4 0 .7-.8 1.1-.8s2 .8 2 1.3-.9 1.5-1.9 1.5c-2.4 0-5.8-3.6-5.8-6 0-1 .9-2 1.5-2z" fill="#fff"/></svg>
    18775206348
  </div>
  <p class="abs back__address">4519 Birchwold Trail Pkwy Unit#312, Chilliwack, BC, V2R 0K7</p>
</section>

</body>
</html>
```